I sell Finches---picture of White Finch Bird----

I raise and sell light color and white Finch - need card to give to Pet shops with my name - Lorna Pettigrew, address: 271 North Ardmore Ln. Santa Barbara, Ca. 93187 - phone - 805-479-3816. All birds raised and nourished in large outside aviary--very healthy and cared for. Would like card to be shiny red with bold print in Broadway font----purple bold print on red card. Design options open - you know best. Would like a picture or pictures of Finches - light or white in color.

Industry/Entity Type

Pet

Contact Information for Business Card

THE WREN KEEPER (LARGE, BOLD BROADWAY PRINT)

```html
<!DOCTYPE html>
<html lang="en">
<head>
<meta charset="utf-8">
<title>The Wren Keeper – Business Card</title>
<link href="https://fonts.googleapis.com/css2?family=PT+Sans:wght@400;700&display=swap" rel="stylesheet">
<style>
  :root {
    --backdrop: #3b3b3b;
    --card-white: #ffffff;
    --card-red: #d01a2c;
    --ink-purple: #3a2277;
    --icon-red: #d01a2c;
    --frame-white: #fbfbfb;
    --photo-tone-light: #d9d9d6;
    --photo-tone-dark: #a9aaa6;
  }
  * { box-sizing: border-box; margin: 0; padding: 0; }
  html, body {
    width: 1200px; height: 1131px; overflow: hidden;
    background: var(--backdrop);
    font-family: "PT Sans", sans-serif;
  }
  .canvas { position: relative; width: 1200px; height: 1131px; }
  .business-card {
    position: absolute; left: 100px; top: 280px;
    width: 1000px; height: 572px;
    background: var(--card-white);
    box-shadow: 0 10px 30px rgba(0,0,0,.45);
    overflow: hidden;
  }
  .photo-panel {
    position: absolute; left: 0; top: 0; width: 440px; height: 100%;
    background: var(--card-red);
  }
  .photo-frame {
    position: absolute;
    background: var(--frame-white);
    padding: 10px;
    box-shadow: 2px 4px 10px rgba(0,0,0,.35);
  }
  .photo-frame .photo {
    width: 100%; height: 100%;
    background: linear-gradient(160deg, var(--photo-tone-light) 0%, var(--photo-tone-dark) 100%);
  }
  .photo-frame--top {
    left: 70px; top: 40px; width: 350px; height: 230px;
    transform: rotate(-5deg);
  }
  .photo-frame--bottom {
    left: 40px; top: 230px; width: 370px; height: 270px;
    transform: rotate(-3deg);
  }
  .info-panel {
    position: absolute; left: 440px; top: 0; right: 0; height: 100%;
    padding: 70px 50px 0 60px;
    color: var(--ink-purple);
  }
  .brand-name {
    font-weight: 700; font-size: 66px; line-height: 1.0;
    letter-spacing: -1px;
  }
  .brand-rule {
    margin-top: 28px; width: 440px; height: 2px; background: var(--ink-purple);
  }
  .owner-name {
    margin-top: 34px; font-weight: 400; font-size: 42px; padding-left: 20px;
  }
  .contact { margin-top: 38px; font-size: 29px; line-height: 1.1; }
  .contact-row { display: flex; align-items: flex-start; gap: 12px; margin-bottom: 14px; }
  .contact-row svg { flex: none; margin-top: 5px; }
  .contact-address { font-style: normal; }
</style>
</head>
<body>
<div class="canvas">
  <article class="business-card">
    <section class="photo-panel">
      <div class="photo-frame photo-frame--top">
        <div class="photo" role="img" aria-label="Photo of a grey finch perched on a ring"></div>
      </div>
      <div class="photo-frame photo-frame--bottom">
        <div class="photo" role="img" aria-label="Photo of two white finches sitting on a perch"></div>
      </div>
    </section>
    <section class="info-panel">
      <h1 class="brand-name">The Wren<br>Keeper</h1>
      <div class="brand-rule"></div>
      <p class="owner-name">Lorna Pettigrew</p>
      <div class="contact">
        <div class="contact-row">
          <svg width="20" height="22" viewBox="0 0 20 22" aria-hidden="true">
            <rect x="2" y="1" width="16" height="20" rx="2" fill="var(--icon-red)"/>
            <circle cx="10" cy="9" r="3" fill="#fff"/>
            <rect x="5" y="14" width="10" height="3" rx="1.5" fill="#fff"/>
          </svg>
          <address class="contact-address">271 North Ardmore Ln.<br>Santa Barbara, Ca. 93187</address>
        </div>
        <div class="contact-row">
          <svg width="20" height="22" viewBox="0 0 24 24" aria-hidden="true">
            <path fill="var(--icon-red)" d="M6.6 10.8a15.1 15.1 0 0 0 6.6 6.6l2.2-2.2c.3-.3.7-.4 1-.2 1.1.4 2.3.6 3.6.6.6 0 1 .4 1 1V20c0 .6-.4 1-1 1A17 17 0 0 1 3 4c0-.6.4-1 1-1h3.5c.6 0 1 .4 1 1 0 1.3.2 2.5.6 3.6.1.3 0 .7-.2 1z"/>
          </svg>
          <span>(805) 479-3816</span>
        </div>
      </div>
    </section>
  </article>
</div>
</body>
</html>
```